Non-fiction book about abuse and survival, needs cover design

This book is about me, and a lifetime of abuse that I survived. The goal is to help others in abusive situations break the cycle of shame that accompanies unhealthy and toxic relationships. I want the cover to illustrate a vast and sometimes scary world where we victims feel alone. It's up to us to choose our destiny, and sometimes we must do that when others don't agree. But there is hope. No longer do we need to believe the lie that something broken is better than nothing at all. After reading this, others will learn to trust their intuition, and how to avoid the pitfalls and red flags of toxic relationships. I want the cover to also show strength, hope, and positivity in the face of adversity. The picture of me (attached) is a good start to show a great big and sometimes frightening world a victim of abuse lives in. I love nature photos, but it's not a requirement for this project. I prefer simple designs. Thank you so much!

Target Market(s)

Survivors of abuse, at risk youth, and friends/family with loved ones who are abused

Requirements
Must have
• Title: The Lantern Keeper
Subtitle: Leave the Crooked Road That Runs Past Every Open Gate You Were Shown
Nice to have
• Outdoor scenery, open spaces.

```html
<!DOCTYPE html>
<html lang="en">
<head>
<meta charset="utf-8">
<title>The Lantern Keeper — Book Cover</title>
<link rel="stylesheet" href="https://fonts.googleapis.com/css2?family=Cinzel:wght@400;500&display=swap">
<style>
  :root {
    --navy: #1f3d5e;
    --ink: #1a1d22;
    --paper: #f4f5f7;
    --sky: #f3f7fa;
    --mist: #c8d8e1;
    --lake: #3c6b7f;
    --ridge: #2b4f5f;
  }
  html, body {
    margin: 0;
    padding: 0;
    width: 800px;
    height: 1200px;
    overflow: hidden;
    background: var(--navy);
  }
  .cover {
    position: relative;
    width: 800px;
    height: 1200px;
    overflow: hidden;
    background: var(--navy);
    font-family: "Cinzel", "Trajan Pro", serif;
  }
  .cover__scene {
    position: absolute;
    left: 0;
    top: 0;
    width: 800px;
    height: 764px;
    background:
      linear-gradient(to bottom, rgba(255,255,255,0) 62%, #ffffff 88%),
      radial-gradient(ellipse 300px 520px at 50% 62%, var(--sky) 55%, var(--mist) 72%, var(--lake) 88%, var(--ridge) 100%);
  }
  .cover__subtitle {
    position: absolute;
    left: 0;
    top: 686px;
    width: 800px;
    margin: 0;
    text-align: center;
    color: var(--ink);
    font-size: 23px;
    font-weight: 400;
    font-variant: small-caps;
    letter-spacing: 1.6px;
    line-height: 31px;
  }
  .cover__title {
    position: absolute;
    left: 0;
    top: 750px;
    width: 800px;
    height: 340px;
  }
  .cover__title text {
    fill: var(--paper);
    font-family: "Cinzel", "Trajan Pro", serif;
  }
  .cover__author {
    position: absolute;
    left: 0;
    top: 1108px;
    width: 800px;
    margin: 0;
    text-align: center;
    color: var(--paper);
    font-size: 38px;
    font-weight: 400;
    letter-spacing: 1px;
  }
</style>
</head>
<body>
  <main class="cover">
    <div class="cover__scene" role="img" aria-label="Photograph of a pale portrait blended with a mountain lake valley under a soft sky"></div>

    <p class="cover__subtitle">Leave the Crooked Road That Runs Past Every<br>Open Gate You Were Shown</p>

    <svg class="cover__title" viewBox="0 0 800 340" role="heading" aria-level="1" aria-label="The Lantern Keeper">
      <text class="cover__title-the" x="400" y="52" text-anchor="middle" font-size="44" letter-spacing="2">THE</text>
      <text class="cover__title-main" x="20" y="182" font-size="150" textLength="760" lengthAdjust="spacingAndGlyphs">LANTERN</text>
      <text class="cover__title-main" x="70" y="320" font-size="150" textLength="660" lengthAdjust="spacingAndGlyphs">KEEPER</text>
    </svg>

    <p class="cover__author">MARISOL FENWICK</p>
  </main>
</body>
</html>
```